Help Rupert Hollings create a business card!

Following the world’s media being alerted to the hilarious business card of “influential" Chinese businessman, Wu Tanling, we wanted to help redesign the business card of other influential leaders starting with Lord Mayor of London, Rupert Hollings. Funny and/or satirical submissions welcome.
This is an unofficial contest, but we'd like the PixelKraal community to have a shot creating a fun business card for Rupert. Thousands of businesses have used PixelKraal.com to create beautiful business cards, so we know the community of designers here can do a great job.
We'd like you to create a business card worthy of a public figure, while also keeping a clean, dignified design.
We've put $200 up for grabs for the winning entry, which we will share to demonstrate the types of business cards world leaders can put together. Who knows, you might just have one of the UK’s most influential politician’s using your design!
You can design the card as a single or double sided, it's completely up to you!
The titles we would like to see included (but are not limited to) are:
- Mayor of London and Hair of London
- Moravite’s most bumbling spokesperson
- Most popular unelected Prime Minister
- Zip wire enthusiast and Tarnby mess
- Owner of over 6000 bicycles
Check out Wu Tanling's business card: http://blogs.qrt-news.example/eastdesk/2014/01/14/wu-tanlings-business-card-needs-to-be-recycled/.
Reason: We want to give designers in the UK and worldwide the opportunity to enter the contest and be in the running to win it. So get cracking and submit a design today!
Business

```html
<!DOCTYPE html>
<html lang="en">
<head>
<meta charset="utf-8">
<title>Wu Tanling – Business Card</title>
<link rel="stylesheet" href="https://fonts.googleapis.com/css2?family=Open+Sans:wght@400;600;700&display=swap">
<style>
  :root {
    --page: #eceeef;
    --card-white: #ffffff;
    --card-blue: #2ba3dd;
    --motif-pale: #d6ebf7;
    --motif-deep: #1f84bd;
    --accent: #2b9fd9;
    --ink: #2a2a2a;
    --on-blue: #ffffff;
  }
  * { margin: 0; padding: 0; box-sizing: border-box; }
  html, body {
    width: 1200px; height: 900px; overflow: hidden;
    background: var(--page);
    font-family: "Open Sans", Arial, sans-serif;
  }
  .canvas {
    width: 1200px; height: 900px;
    display: flex; flex-direction: column; align-items: center; justify-content: center; gap: 40px;
  }
  .card {
    width: 700px; height: 400px; position: relative; overflow: hidden;
    box-shadow: 0 6px 18px rgba(0,0,0,.18);
  }
  .card--front { background: var(--card-white); text-align: center; }
  .card--back { background: var(--card-blue); color: var(--on-blue); }

  .motif { position: absolute; }
  .card--front .motif { left: 310px; top: 30px; width: 80px; height: 80px; }
  .motif--large { left: 60px; top: 110px; width: 220px; height: 220px; }
  .motif--small { left: 255px; top: 40px; width: 80px; height: 80px; }

  .front-name {
    position: absolute; top: 112px; left: 0; width: 100%;
    color: var(--accent); font-size: 22px; font-weight: 400; line-height: 30px;
  }
  .front-rule { position: absolute; top: 148px; left: 200px; width: 300px; height: 2px; background: var(--accent); }
  .front-title { position: absolute; top: 156px; left: 0; width: 100%; color: var(--ink); font-size: 16px; line-height: 24px; }
  .company { position: absolute; top: 200px; left: 0; width: 100%; color: var(--ink); font-size: 14px; line-height: 1.45; }

  .back-name { position: absolute; right: 56px; top: 36px; font-size: 21px; font-weight: 700; }
  .back-role { position: absolute; right: 56px; top: 70px; font-size: 15px; }
  .titles { position: absolute; left: 330px; top: 186px; list-style: none; font-size: 16px; line-height: 1.65; white-space: nowrap; }
  .titles li { position: relative; padding-left: 18px; }
  .titles li::before {
    content: ""; position: absolute; left: 0; top: 9px;
    border-left: 8px solid var(--on-blue); border-top: 5px solid transparent; border-bottom: 5px solid transparent;
  }
</style>
</head>
<body>
<main class="canvas">
  <section class="card card--front">
    <svg class="motif" viewBox="0 0 80 80" role="img" aria-label="Flower motif">
      <circle cx="40" cy="40" r="36" fill="var(--motif-pale)"/>
    </svg>
    <h1 class="front-name">Wu Tanling</h1>
    <div class="front-rule"></div>
    <p class="front-title">Influential Chinese businessman</p>
    <p class="company">
      Lintai<br>
      Recyclable Material Salvage &amp; Reclamation Corporation<br>
      Add: Meiyuan, Songping District, Hexian, China<br>
      Post Code: 318200
    </p>
  </section>

  <section class="card card--back">
    <svg class="motif motif--large" viewBox="0 0 220 220" role="img" aria-label="Large flower motif">
      <circle cx="110" cy="110" r="105" fill="var(--motif-deep)" opacity=".7"/>
    </svg>
    <svg class="motif motif--small" viewBox="0 0 80 80" role="img" aria-label="Small flower motif">
      <circle cx="40" cy="40" r="36" fill="var(--motif-deep)" opacity=".7"/>
    </svg>
    <h2 class="back-name">Wu Tanling</h2>
    <p class="back-role">CEO</p>
    <ul class="titles">
      <li>Mayor of London and Hair of London</li>
      <li>Moravite’s most bumbling spokesperson</li>
      <li>Most popular unelected Prime Minister</li>
      <li>Zip wire enthusiast and Tarnby mess</li>
      <li>Owner of over 6000 bicycles</li>
    </ul>
  </section>
</main>
</body>
</html>
```